Law Firm Needs a new Website Design

We need a new website design for our law firm located in Manhattan (Law Offices of Tobias R. Venkland, PLLC).
We have an existing logo that we will to continue using, which can be found in www.VenklandLaw.example.
The Prime Counsel, Top Advocates Logo should also be reflected near the bottom of the Home page.
The website will be 6 pages.

Deliverables:
I want a
1) home page,
2) About Us/Practice Areas page,
3) attorneys,
4) News and Articles page, and
5) Contact and Directions/Privacy Policy page.

The colors of my logo should be in the website.
I also like a touch of black and red.

The website should project "excellence."
We seek to provide the highest quality legal services.
We handle estate planning, wills, trusts, planning for people with disabilities, asset protection and preservation, Medicaid planning, hospital safe discharge, nursing home placement, powers of attorney, health care proxies, living wills, guardianships, probate, estate administration and related litigation.

I would like the colors of my Logo used (including shading where appropriate).
I also want some black on the borders and/or bottom and some red touches throughout the page.

My Logo should appear everywhere that "Law Offices Of Tobias R. Venkland, PLLC" appears.
I want the badges for Prime counsel, Top Advocates, Top Legal Practices, and ZELQ on the Home page.
I do not want too much text on the home page.

We would also like the website to have coding.
The final design should also communicate quality, expertise and stability.
Great start so far by the people who submitted designs.
Thank you.

Industry/Entity Type

Law Firm

Coding

Coded - Design and coding required

Number of Pages Required

5+ page

Colors
3276b5
ec1f27
474747

Requirements
Must have
• Please use my logo each time you mention Law Offices of Tobias R. Venkland, PLLC. Please include the Primecounsel, Top Advocates, Top Legal Practices and Zelq rating Badges on the web home page. I only wish to be contacted by phone. I am not including testimonials and am only using the New York City address.
Nice to have
• Prefer illustrations to photos regarding practice areas
Should not have
• Testimonials, contact me by email, free consultation.

```html
<!DOCTYPE html>
<html lang="en">
<head>
<meta charset="utf-8">
<title>Law Offices of Tobias R. Venkland, PLLC</title>
<link href="https://fonts.googleapis.com/css2?family=Libre+Baskerville:wght@400;700&family=Montserrat:wght@400;500&display=swap" rel="stylesheet">
<style>
:root{
  --brand-blue:#3276b5;
  --navy:#1f3a68;
  --accent-red:#ec1f27;
  --ink:#474747;
  --dark:#111111;
  --paper:#f5f5f5;
  --line:#e2e2e2;
  --badge-grey:#9a9a9a;
}
*{margin:0;padding:0;box-sizing:border-box}
html,body{width:762px;height:1200px;overflow:hidden;background:#fff}
.page{position:relative;width:762px;height:1200px;overflow:hidden;font-family:"Libre Baskerville",Georgia,serif;color:var(--ink)}
.hero{position:absolute;left:0;top:0;width:762px;height:347px}
.hero-photo{position:absolute;inset:0;background:linear-gradient(100deg,#e7542f 0%,#f0a35a 16%,#e86a6a 32%,#e5a0a6 52%,#c55d6a 72%,#4a3540 90%,#1f2027 100%)}
.hero-veil{position:absolute;inset:0;background:radial-gradient(ellipse 300px 180px at 50% 45%,rgba(255,255,255,.85),rgba(255,255,255,0) 100%)}
.brand{position:absolute;left:0;width:100%;text-align:center;color:var(--navy)}
.brand-mark{display:block;margin:0 auto 6px;width:22px;height:22px;background:var(--navy)}
.brand .pre{font-family:"Montserrat",sans-serif;font-size:10px;letter-spacing:1px}
.brand .name{font-size:18px;letter-spacing:1px;line-height:1.25}
.brand .suffix{font-family:"Montserrat",sans-serif;font-size:8px;letter-spacing:2px}
.hero .brand{top:74px}
.hero-intro{position:absolute;left:261px;top:165px;width:240px;text-align:center;font-size:6.6px;line-height:10px;color:#3c3c3c}
.contact-btn{position:absolute;left:324px;top:224px;width:114px;height:23px;background:linear-gradient(90deg,#1f3a68,#3276b5);color:#fff;font-size:7.5px;letter-spacing:.6px;text-align:center;line-height:23px}
.scroll-cue{position:absolute;left:372px;top:302px}
.topbar{position:absolute;left:0;top:347px;width:762px;height:40px;background:#fff;border-bottom:1px solid var(--line)}
.phone{position:absolute;left:148px;top:14px;font-size:7.8px;color:var(--dark);display:flex;align-items:center;gap:5px}
.topbar .mark{position:absolute;left:372px;top:10px;width:18px;height:18px;background:var(--navy)}
.menu{position:absolute;left:601px;top:14px}
.services{position:absolute;left:0;top:387px;width:762px;height:246px;background:linear-gradient(90deg,#eef0ef 0%,#fafafa 25%,#fff 50%,#fafafa 75%,#f0f0f0 100%)}
.services-room{position:absolute;left:0;top:40px;width:150px;height:200px;background:radial-gradient(ellipse at 50% 50%,#e4e9e3,rgba(255,255,255,0) 70%)}
.section-title{position:absolute;left:0;width:100%;text-align:center;font-size:13.5px;color:#2b2b2b;letter-spacing:.4px}
.section-rule{position:absolute;left:363px;width:36px;height:1.5px;background:var(--accent-red)}
.services .section-title{top:29px}
.services .section-rule{top:55px}
.service-grid{position:absolute;left:148px;top:79px;width:468px;display:grid;grid-template-columns:repeat(4,117px);grid-template-rows:44px 44px 44px}
.service-grid div{display:flex;align-items:center;justify-content:center;text-align:center;font-size:6.4px;line-height:8.2px;color:#333;text-transform:uppercase;padding:0 8px;border-right:1px solid var(--line);border-bottom:1px solid var(--line)}
.service-grid div:nth-child(4n){border-right:none}
.service-grid div:nth-child(n+9){border-bottom:none}
.about{position:absolute;left:0;top:632px;width:762px;height:329px;background:var(--paper);border-top:1.5px solid var(--accent-red)}
.about .mark{position:absolute;left:369px;top:41px;width:24px;height:24px;background:var(--navy)}
.about .section-title{top:79px;font-weight:700}
.about .section-rule{top:99px}
.about-copy{position:absolute;left:186px;top:116px;width:390px;text-align:center;font-size:6.6px;line-height:10.2px;color:#444}
.about-copy p{margin-bottom:10px}
.about-copy .signature{font-weight:700;color:#333}
.badges{position:absolute;left:0;top:961px;width:762px;height:96px;background:#ececec}
.badge-text{position:absolute;top:28px;font-size:14px;color:var(--badge-grey);letter-spacing:-.2px}
.badge-shape{position:absolute;background:#b8b8b8}
.footer{position:absolute;left:0;top:1057px;width:762px;height:46px;background:var(--dark);font-family:"Montserrat",sans-serif}
.office{position:absolute;left:150px;top:12px}
.office h4{font-size:5.2px;color:var(--brand-blue);font-weight:500;letter-spacing:.3px;margin-bottom:5px}
.office p{font-size:4.4px;line-height:6.5px;color:#ddd}
.footer-nav{position:absolute;right:148px;top:12px;font-size:5.2px;color:#fff;letter-spacing:.3px}
.footer-nav span.sep{margin:0 5px}
.footer-nav .current{color:var(--brand-blue)}
.social{position:absolute;right:148px;top:28px;display:flex;gap:9px}
.social i{display:block;width:6px;height:6px;border-radius:50%;background:#fff}
.closing{position:absolute;left:0;top:1103px;width:762px;height:97px;background:#fff}
.closing .brand{top:6px}
.closing .brand .name{font-size:13px}
.closing .brand .pre{font-size:7px}
.closing .brand .suffix{font-size:6px}
.closing .brand-mark{width:20px;height:20px;margin-bottom:5px}
.copyright{position:absolute;left:0;top:67px;width:100%;text-align:center;font-family:"Montserrat",sans-serif;font-size:4.6px;color:#999}
</style>
</head>
<body>
<div class="page">
  <section class="hero">
    <div class="hero-photo" role="img" aria-label="Photo of an attorney signing documents at a desk in warm light"></div>
    <div class="hero-veil"></div>
    <div class="brand">
      <span class="brand-mark"></span>
      <div class="pre">Law Offices of</div>
      <div class="name">TOBIAS R. VENKLAND</div>
      <div class="suffix">PLLC</div>
    </div>
    <p class="hero-intro">Our firm was founded in 1993 by Tobias R. Venkland, a member of the National Guild of Elder Counsel (NGEC) and an elder law practitioner for over 19 years.</p>
    <div class="contact-btn">CONTACT US</div>
    <svg class="scroll-cue" width="18" height="10" viewBox="0 0 18 10"><polyline points="1,1 9,8 17,1" fill="none" stroke="#7a6d72" stroke-width="1"/></svg>
  </section>

  <header class="topbar">
    <div class="phone">
      <svg width="9" height="9" viewBox="0 0 24 24"><path d="M6.6 10.8c1.4 2.8 3.8 5.1 6.6 6.6l2.2-2.2c.3-.3.7-.4 1-.2 1.1.4 2.3.6 3.6.6.6 0 1 .4 1 1V20c0 .6-.4 1-1 1C10.6 21 3 13.4 3 4c0-.6.4-1 1-1h3.5c.6 0 1 .4 1 1 0 1.3.2 2.5.6 3.6.1.3 0 .7-.2 1L6.6 10.8z" fill="#1f3a68"/></svg>
      (212) 555-0148
    </div>
    <span class="mark"></span>
    <svg class="menu" width="12" height="10" viewBox="0 0 12 10"><rect y="0" width="12" height="1.5" fill="#1f3a68"/><rect y="4.2" width="12" height="1.5" fill="#1f3a68"/><rect y="8.5" width="12" height="1.5" fill="#1f3a68"/></svg>
  </header>

  <section class="services">
    <div class="services-room" role="img" aria-label="Soft office interior with a potted plant"></div>
    <h2 class="section-title">SERVICES WE HANDLE</h2>
    <span class="section-rule"></span>
    <div class="service-grid">
      <div>Estate Planning</div>
      <div>Trusts &amp; Wills</div>
      <div>Probate</div>
      <div>Health Care<br>Proxies</div>
      <div>Guardianships</div>
      <div>Powers of<br>Attorney</div>
      <div>Medicaid<br>Planning</div>
      <div>Nursing Home<br>Placement</div>
      <div>Asset Protection<br>and Preservation</div>
      <div>Estate<br>Administration and<br>Related Litigation</div>
      <div>Planning for<br>People with<br>Disabilities</div>
      <div>Hospital Safe<br>Discharge</div>
    </div>
  </section>

  <section class="about">
    <span class="mark"></span>
    <h2 class="section-title">ABOUT US</h2>
    <span class="section-rule"></span>
    <div class="about-copy">
      <p>Our firm was founded in 1993 by Tobias R. Venkland, a member of the National Guild of Elder Counsel (NGEC) and an elder law practitioner for over 19 years. Our firm is uniquely positioned to provide quality legal advice and representation in regards to estate planning, wills, trusts, planning for people with disabilities, asset protection and preservation, Medicaid planning, hospital safe discharge, nursing home placement, powers of attorney, health care proxies, living wills, guardianships, probate, estate administration and related litigation.</p>
      <p>Our familiarity with entitlement programs such as Medicaid and the statutes and regulations pertaining to them, our sensitivity to the problems and needs of seniors and our access to geriatric care managers enable us to help families preserve their life savings while planning for the care of a spouse, a parent or loved one who has dementia, Alzheimer's or other long-term health care needs.</p>
      <p>We care about our clients and believe in cultivating long-term relationships. We strive to maintain the dignity, independence and well-being of our clients and respond to them quickly with the consideration and respect they deserve.</p>
      <p class="signature">Tobias R. Venkland</p>
    </div>
  </section>

  <section class="badges">
    <span class="badge-text" style="left:172px">Prime Counsel</span>
    <span class="badge-text" style="left:288px">Top Advocates</span>
    <span class="badge-shape" style="left:433px;top:25px;width:46px;height:46px;border-radius:4px"></span>
    <span class="badge-shape" style="left:525px;top:25px;width:48px;height:48px;border-radius:50%"></span>
  </section>

  <footer class="footer">
    <div class="office">
      <h4>MAIN OFFICE</h4>
      <p>118 Harlow Street, Suite 1402<br>New York, New York 10017</p>
    </div>
    <nav class="footer-nav">
      <span class="current">HOME</span><span class="sep">|</span>SERVICES<span class="sep">|</span>ATTORNEYS<span class="sep">|</span>NEWS<span class="sep">|</span>CONTACT US
    </nav>
    <div class="social"><i></i><i></i><i></i></div>
  </footer>

  <div class="closing">
    <div class="brand">
      <span class="brand-mark"></span>
      <div class="pre">Law Offices of</div>
      <div class="name">TOBIAS R. VENKLAND</div>
      <div class="suffix">PLLC</div>
    </div>
    <div class="copyright">Copyrights© 2009-2016</div>
  </div>
</div>
</body>
</html>
```